Individual Signage for Grape Tippers

We operate 11 tippers that we require signage for. Each tipper has it's own "name" and I'd like the signage to reflect that name.
The tippers are currently referred to using their numbers, 1-11, but we would like to have some fun with them and have created names and personalities for each tipper.
The tippers are all painted white, so the use of bright, bold, powerful colours and images would be fantastic.
Be mindful of each tipper's name and develop a personality that fits and reflects it.
We MUST HAVE a design for EACH tipper.
I am happy to pay for EACH successful design. You can choose just one Tipper to design if you like.

Target Market(s)

My husband! 50yo

Industry/Entity Type

Trucking Company

Font styles to use
Decorative

Colors

Designer to choose colors to be used in the design.

Requirements
Must have
• The tipper names are as follows:
• The Chief
• Grindle
• Rattler
• Mud Flap
• Hexamore
• The Brute
• The Rascal
• Squidwinkle
• The Owl
• Rex 7
• Maud
• One sign for each tipper. Signage needs to fit the name of the tipper. The tippers are all white and we intend to have the winning designs printed and applied to the tipper professionally.
• The finished product will be on a large scale.
Nice to have
• Bold Colours
Should not have
• Nothing too girly, or sexist (no nudes etc).

```html
<!DOCTYPE html>
<html lang="en">
<head>
<meta charset="utf-8">
<title>Squidwinkle – Tipper Signage</title>
<link rel="stylesheet" href="https://fonts.googleapis.com/css2?family=Rye&display=swap">
<style>
  :root {
    --page: #e9ecee;
    --cream: #f4f2e3;
    --sky-a: #b3e3f7;
    --sky-b: #a5dcf3;
    --teal-ink: #1d6b6d;
    --teal-mid: #4db5c0;
    --teal-soft: #bfe6ee;
  }
  html, body {
    margin: 0;
    width: 1200px;
    height: 674px;
    overflow: hidden;
    background: var(--page);
  }
  .canvas {
    position: relative;
    width: 1200px;
    height: 674px;
  }
  .tipper-sign {
    position: absolute;
    left: 0;
    top: 197px;
    width: 1200px;
    height: 280px;
    background: var(--cream);
    overflow: hidden;
  }
  .sign-waves {
    position: absolute;
    left: 0;
    bottom: 0;
    width: 100%;
    height: 130px;
    background:
      radial-gradient(circle at 15px 0, var(--cream) 12px, var(--teal-ink) 12.5px, var(--teal-ink) 13.2px, transparent 13.8px) 0 0 / 30px 14px repeat-x,
      repeating-linear-gradient(90deg, var(--sky-a) 0 70px, var(--sky-b) 70px 140px);
  }
  .sign-name {
    position: absolute;
    left: 84px;
    top: 62px;
    margin: 0;
    font-family: "Rye", serif;
    font-weight: 400;
    font-size: 72px;
    line-height: 1;
    letter-spacing: 16px;
    text-transform: uppercase;
    color: var(--teal-ink);
    white-space: nowrap;
  }
  .badge-art {
    position: absolute;
    left: 872px;
    top: 40px;
    width: 250px;
    height: 190px;
    border-radius: 50%;
    background: radial-gradient(ellipse at center, var(--teal-soft) 0%, var(--teal-mid) 75%, var(--teal-ink) 100%);
  }
</style>
</head>
<body>
<div class="canvas">
  <section class="tipper-sign" aria-label="Squidwinkle tipper sign">
    <div class="sign-waves"></div>
    <h1 class="sign-name">Squidwinkle</h1>
    <div class="badge-art" role="img" aria-label="Emblem area: ribbon banner with a porthole framing a curly-tentacled sea creature"></div>
  </section>
</div>
</body>
</html>
```